Web design for Velvet parlour evenings

i would like a classy, elegant website designed for a speed dating events business I am in the progress of starting. I have a logo an would like the webpage to look very sophisticated as I my target market it upper class.
* website needs to be able to be coded easily! thanks

my contact details are:

Email contact@velvetparlourevenings.com.au
Business number 08 7462 3158
Mobile number 0461837295

I would like to have a feature of upcoming speed dating events as i book them listed on my webpage ( an example of this is http://www.quickmeetlounge-example.com.au/speed-dating-adelaide-singles) and on this same website is a contact details form to the right where clients will be filling in their details to forward to me.. Is this possible to have on my website through this process? Also I am looking to have coinbridge payment options?

Business information

Velvet Parlour Evenings
Adelaide CBD, Australia

Velvet parlour evenings is an elegant and sophisticated speed dating organisation. New to Adelaide, we aim to provide a service where you feel pampered and have fun while ‘dating’ with a touch of class! With extensive dating industry experience in Adelaide and North America, founder Marguerite Holloway, has a passion for introducing singles. So, let’s get out there and date with speed! Your soul mate could be at the next table!

more text to come

Reason: Still need changes and designs submitted, also wanting to discuss coding options with designers. I have a domain name and net harbour account set up.

```html
<!DOCTYPE html>
<html lang="en">
<head>
<meta charset="utf-8">
<title>Velvet Parlour Evenings</title>
<link href="https://fonts.googleapis.com/css2?family=Open+Sans:wght@300;400;600&display=swap" rel="stylesheet">
<style>
:root{
  --black:#0d0c0b;
  --gold:#c8963a;
  --gold-light:#e2c98a;
  --gold-dark:#a88436;
  --grey-bg:#e3e3e3;
  --panel:#f7f7f7;
  --line:#dddddd;
  --text:#555555;
  --text-soft:#777777;
  --white:#ffffff;
}
*{margin:0;padding:0;box-sizing:border-box}
html,body{width:861px;height:1200px;overflow:hidden;background:var(--white)}
body{position:relative;font-family:"Open Sans",Arial,sans-serif;color:var(--text)}

/* header */
.site-header{position:absolute;left:0;top:0;width:861px;height:99px;background:var(--black);z-index:3}
.brand-plate{position:absolute;left:333px;top:0;width:196px;height:116px}
.brand-name{position:absolute;left:333px;top:32px;width:196px;text-align:center;color:var(--gold);font-size:15px;font-weight:400;letter-spacing:1.5px;line-height:18px;text-transform:uppercase}
.brand-numbers{position:absolute;left:333px;top:91px;width:196px;text-align:center;color:var(--gold);font-size:8.5px;line-height:12px;letter-spacing:.6px}
.brand-dot{position:absolute;left:424px;top:12px;width:14px;height:14px;border-radius:50%;background:var(--gold)}
.header-contacts{position:absolute;left:572px;top:34px;font-size:9px;color:var(--gold)}
.header-contacts li{list-style:none;display:flex;align-items:center;height:18px}
.header-contacts svg{margin-right:8px}

/* hero */
.hero{position:absolute;left:0;top:99px;width:861px;height:342px;background:linear-gradient(100deg,#3b2a22 0%,#6b5040 28%,#2e211b 48%,#7a5a48 62%,#4b2f2a 80%,#2a1c18 100%)}
.hero-copy{position:absolute;left:113px;top:124px;color:var(--white)}
.hero-kicker{font-size:19px;font-weight:300;line-height:22px}
.hero-title{font-size:31px;font-weight:400;line-height:38px}
.hero-cta{position:absolute;left:111px;top:199px;width:219px;height:37px;border:2px solid rgba(255,255,255,.75);border-radius:5px;background:rgba(0,0,0,.45);color:var(--white);font-size:16px;font-weight:300;line-height:33px;text-align:center}

/* intro */
.intro{position:absolute;left:0;top:441px;width:861px;height:256px;background:var(--grey-bg)}
.intro-title{position:absolute;left:113px;top:35px;font-size:21px;font-weight:300;color:var(--gold)}
.intro-text{position:absolute;left:113px;top:78px;width:366px;font-size:11.2px;line-height:19.8px;font-weight:300;color:#4a4a4a;text-align:justify}
.intro-photos{position:absolute;left:525px;top:30px;width:230px;height:175px}

/* ribbon */
.ribbon{position:absolute;left:300px;top:670px;width:244px;height:46px;z-index:2}
.ribbon-label{position:absolute;left:300px;top:682px;width:244px;text-align:center;font-size:13px;color:#6b5222;letter-spacing:.3px;z-index:2}

/* events area */
.events{position:absolute;left:0;top:697px;width:861px;height:461px;background:radial-gradient(ellipse at 30% 30%,#6a3d1c 0%,#3b200f 45%,#1d110a 100%)}
.events-table{position:absolute;left:113px;top:751px;width:386px;height:363px;background:var(--panel);border:1px solid #cfcfcf}
.table-head{position:absolute;left:0;top:0;width:100%;height:33px;border-bottom:1px solid var(--line);font-size:10.5px;color:var(--gold)}
.table-head span{position:absolute;top:10px}
.event-row{position:absolute;left:0;width:100%;height:66px;border-bottom:1px solid var(--line);font-size:8.2px;line-height:13px;color:var(--text-soft)}
.event-row:last-child{border-bottom:none}
.event-thumb{position:absolute;left:7px;top:13px;width:39px;height:39px;border-radius:3px;background:linear-gradient(135deg,#8a6a4a,#3d2a1c)}
.event-row .title{color:#444}
.event-row .col{position:absolute;top:13px;white-space:nowrap}
.status{color:var(--gold)}

/* finder form */
.finder{position:absolute;left:537px;top:751px;width:211px;height:363px;background:var(--panel);border:1px solid #cfcfcf}
.finder-head{height:33px;border-bottom:1px solid var(--line);font-size:10.5px;color:#7a5a20;padding:10px 0 0 10px}
.finder-intro{position:absolute;left:10px;top:41px;width:190px;font-size:8px;line-height:12px;color:var(--text-soft)}
.finder-divider{position:absolute;left:0;width:100%;border-top:1px dashed #d5d5d5}
.field{position:absolute;left:0;width:100%;height:20px}
.field label{position:absolute;right:121px;top:4px;font-size:8.8px;color:#9a7530;white-space:nowrap}
.input{position:absolute;top:0;height:19px;background:var(--white);border:1px solid #d0d0d0;font-size:7.6px;color:#666;line-height:17px;padding-left:4px;white-space:nowrap}
.select{padding-right:12px}
.select::after{content:"";position:absolute;right:4px;top:7px;border:3px solid transparent;border-top-color:#777}
.and{position:absolute;left:141px;top:4px;font-size:8.8px;color:#666}
.finder-btn{position:absolute;left:10px;top:322px;width:194px;height:30px;border-radius:3px;background:linear-gradient(#e4cc8c,#c7a24c);border:1px solid var(--gold-dark);color:#6b5222;font-size:12.5px;text-align:center;line-height:28px}

/* footer */
.site-footer{position:absolute;left:0;top:1158px;width:861px;height:42px;background:var(--grey-bg);font-size:7.3px;color:#777}
.site-footer .left{position:absolute;left:112px;top:16px}
.site-footer .right{position:absolute;right:113px;top:16px}
</style>
</head>
<body>

<header class="site-header">
  <svg class="brand-plate" viewBox="0 0 196 116" aria-hidden="true">
    <path d="M0 0 H196 V100 L184 116 H12 L0 100 Z" fill="#0d0c0b"/>
    <path d="M0 99 L12 115 H184 L196 99" fill="none" stroke="#3a3a3a" stroke-width="1.5"/>
  </svg>
  <span class="brand-dot"></span>
  <div class="brand-name">Velvet Parlour<br>Evenings</div>
  <div class="brand-numbers">B:0874623158 &nbsp;M:0461837295</div>
  <ul class="header-contacts">
    <li>
      <svg width="12" height="12" viewBox="0 0 12 12"><circle cx="6" cy="6" r="6" fill="#c8963a"/><path d="M4 3.2c.4-.3.8-.2 1 .2l.4.9c.1.3 0 .5-.2.7l-.3.3c.3.7.8 1.2 1.5 1.5l.3-.3c.2-.2.4-.3.7-.2l.9.4c.4.2.5.6.2 1l-.4.4C7 8.8 3.2 5 3.6 3.6z" fill="#0d0c0b"/></svg>
      08 7462 3158 - 0461837295
    </li>
    <li>
      <svg width="12" height="12" viewBox="0 0 12 12"><circle cx="6" cy="6" r="6" fill="#c8963a"/><rect x="3" y="4" width="6" height="4.2" fill="#0d0c0b"/><path d="M3 4l3 2.3L9 4" fill="none" stroke="#c8963a" stroke-width=".7"/></svg>
      contact@velvetparlourevenings.com.au
    </li>
  </ul>
</header>

<section class="hero" role="img" aria-label="Photo of an elegantly dressed couple smiling over a menu at a candlelit restaurant table">
  <div class="hero-copy">
    <div class="hero-kicker">Have fun while dating</div>
    <div class="hero-title">with a touch of class</div>
  </div>
  <div class="hero-cta">Check out upcoming events</div>
</section>

<section class="intro">
  <h2 class="intro-title">Your soul mate could be at the next table</h2>
  <p class="intro-text">Velvet parlour evenings is an elegant and sophisticated speed dating organisation. New to Adelaide, we aim to provide a service where you feel pampered and have fun while ‘dating’ with a touch of class! With extensive dating industry experience in Adelaide and North America, founder Marguerite Holloway, has a passion for introducing singles. So, let’s get out there and date with speed! Your soul mate could be at the next table!</p>
  <svg class="intro-photos" viewBox="0 0 230 175" role="img" aria-label="Three round photos of couples enjoying dinner dates">
    <defs>
      <linearGradient id="p1" x1="0" y1="0" x2="1" y2="1"><stop offset="0" stop-color="#7a5a44"/><stop offset="1" stop-color="#2e221c"/></linearGradient>
      <linearGradient id="p2" x1="0" y1="0" x2="1" y2="1"><stop offset="0" stop-color="#b9a99a"/><stop offset="1" stop-color="#3a3638"/></linearGradient>
      <linearGradient id="p3" x1="0" y1="0" x2="1" y2="1"><stop offset="0" stop-color="#c79a6a"/><stop offset="1" stop-color="#4a2c1c"/></linearGradient>
    </defs>
    <circle cx="66" cy="58" r="59" fill="url(#p1)" stroke="#fff" stroke-width="3"/>
    <circle cx="166" cy="104" r="57" fill="url(#p2)" stroke="#fff" stroke-width="3"/>
    <circle cx="82" cy="139" r="41" fill="url(#p3)" stroke="#fff" stroke-width="3"/>
  </svg>
</section>

<section class="events" role="img" aria-label="Warmly lit restaurant interior with set tables and booths"></section>

<svg class="ribbon" viewBox="0 0 244 46" aria-hidden="true">
  <defs><linearGradient id="rb" x1="0" y1="0" x2="0" y2="1"><stop offset="0" stop-color="#eed9a2"/><stop offset="1" stop-color="#c9a352"/></linearGradient></defs>
  <path d="M0 10 H44 V40 H8 L18 25 Z" fill="#b68f3e"/>
  <path d="M244 10 H200 V40 H236 L226 25 Z" fill="#b68f3e"/>
  <rect x="44" y="0" width="156" height="38" fill="url(#rb)"/>
  <path d="M44 38 L52 44 V38 Z M200 38 L192 44 V38 Z" fill="#7d6128"/>
</svg>
<div class="ribbon-label">UPCOMING EVENTS</div>

<div class="events-table">
  <div class="table-head">
    <span style="left:8px">Event type &amp; city</span>
    <span style="left:159px">Date &amp; Time</span>
    <span style="left:232px">Age</span>
    <span style="left:283px">Status</span>
    <span style="left:346px">Price</span>
  </div>
  <div style="position:absolute;left:0;top:33px;width:100%">
    <div class="event-row" style="top:0">
      <div class="event-thumb" role="img" aria-label="Restaurant dining room"></div>
      <div class="col" style="left:53px"><span class="title">Speed dating with style</span><br>Linden Dining Room<br>Adelaide</div>
      <div class="col" style="left:161px">04.26.2014<br>7.00pm</div>
      <div class="col" style="left:233px">M : 40-50<br>F : 35-42</div>
      <div class="col status" style="left:284px">2 spaces left</div>
      <div class="col" style="left:346px">$ 95.20</div>
    </div>
    <div class="event-row" style="top:66px">
      <div class="event-thumb" role="img" aria-label="Hotel bar interior"></div>
      <div class="col" style="left:53px"><span class="title">Tall men speed dating</span><br>The Harrow Hotel<br>Adelaide</div>
      <div class="col" style="left:161px">05.03.2014<br>10.00pm</div>
      <div class="col" style="left:233px">M : 30-40<br>F : 25-35</div>
      <div class="col status" style="left:284px">1 spaces left</div>
      <div class="col" style="left:346px">$ 87.15</div>
    </div>
    <div class="event-row" style="top:132px">
      <div class="event-thumb" role="img" aria-label="Guests at a party"></div>
      <div class="col" style="left:53px"><span class="title">Single’s party</span><br>Bar 214, West<br>Adelaide</div>
      <div class="col" style="left:161px">04.26.2014<br>7.00pm</div>
      <div class="col" style="left:233px">M : 40-50<br>F : 35-42</div>
      <div class="col status" style="left:284px">2 spaces left</div>
      <div class="col" style="left:346px">$ 95.20</div>
    </div>
    <div class="event-row" style="top:198px">
      <div class="event-thumb" role="img" aria-label="Restaurant dining room"></div>
      <div class="col" style="left:53px"><span class="title">Speed dating with style</span><br>Linden Dining Room<br>Adelaide</div>
      <div class="col" style="left:161px">04.26.2014<br>7.00pm</div>
      <div class="col" style="left:233px">M : 40-50<br>F : 35-42</div>
      <div class="col status" style="left:284px">2 spaces left</div>
      <div class="col" style="left:346px">$ 95.20</div>
    </div>
    <div class="event-row" style="top:264px">
      <div class="event-thumb" role="img" aria-label="Restaurant dining room"></div>
      <div class="col" style="left:53px"><span class="title">Speed dating with style</span><br>Linden Dining Room<br>Adelaide</div>
      <div class="col" style="left:161px">04.26.2014<br>7.00pm</div>
      <div class="col" style="left:233px">M : 40-50<br>F : 35-42</div>
      <div class="col status" style="left:284px">2 spaces left</div>
      <div class="col" style="left:346px">$ 95.20</div>
    </div>
  </div>
</div>

<form class="finder">
  <div class="finder-head">Let us find you the perfect event</div>
  <p class="finder-intro">Tell us a bit about yourself to see speed dating &amp; singles events that suit you. It’s free !</p>
  <div class="finder-divider" style="top:75px"></div>
  <div class="field" style="top:85px"><label>Name &amp; Surname :</label><div class="input" style="left:95px;width:109px"></div></div>
  <div class="field" style="top:110px"><label>Birth date :</label>
    <div class="input select" style="left:95px;width:31px">MM</div>
    <div class="input select" style="left:130px;width:31px">DD</div>
    <div class="input select" style="left:165px;width:39px">YY</div>
  </div>
  <div class="field" style="top:134px"><label>I live in :</label><div class="input select" style="left:95px;width:109px">Please select one</div></div>
  <div class="field" style="top:158px"><label>I am a :</label><div class="input select" style="left:95px;width:109px">Please select one</div></div>
  <div class="field" style="top:182px"><label>Aged between :</label>
    <div class="input select" style="left:95px;width:42px">Select</div>
    <span class="and">and</span>
    <div class="input select" style="left:161px;width:43px">Select</div>
  </div>
  <div class="field" style="top:206px"><label>My education level :</label><div class="input select" style="left:95px;width:109px">Please select one</div></div>
  <div class="field" style="top:231px"><label>I am a :</label><div class="input select" style="left:95px;width:109px">Please select one</div></div>
  <div class="field" style="top:256px"><label>My height is :</label><div class="input select" style="left:95px;width:109px">Please select one</div></div>
  <div class="field" style="top:280px"><label>Email :</label><div class="input" style="left:95px;width:109px"></div></div>
  <div class="finder-divider" style="top:311px"></div>
  <div class="finder-btn">SUGGEST ME AN EVENT</div>
</form>

<footer class="site-footer">
  <span class="left">© 2014 Velvet Parlour Evenings | All rights reserved</span>
  <span class="right">Phone : 08 7462 3158 - 0461837295 &nbsp;&nbsp;&nbsp; Email : velvetparlour@mailbox-example.com</span>
</footer>

</body>
</html>
```